Flyer designen DIN lang (9,8 x 21 cm): food/ event
Zielgruppe
Wir von taste-the-town bieten kulinarisch-kulturelle Stadtführungen in Deutschland an. Zurzeit bieten wir unserer Touren in 20 Städten an.
Aufgabenstellung
Wir brauchen einen neuen Flyer, da zum einen das Design etwas veraltet ist und zum anderen immer mehr Städte dazu kommen.
Was drauf sein sollte:
- Schönes Bild am besten mit Menschen die essen und Spaß haben (siehe Materialien/ Downoalds) oder Bildvorrat etc.
- taste-the-town Logo
- Text:
a) prägnant: Tickets online www.taste-the-town.com
b) Teaser auf:
1. Verschenken Sie uns als Gutschein (evtl. mit Bild vom Gutschein)
2. Möchten Sie auch Gäste begeistern? Bewerben Sie sich als Tourguide!
- Städte-Auflistung: Augsburg, Bamberg, Berlin, Bonn, Bremen, Dresden, Düsseldorf, Essen, Frankfurt, Hamburg, Hannover, Köln, Leipzig, München, Münster, Nürnberg, Oldenburg, Potsdam, Regensburg und Stuttgart
>> die Städte sollten gut erweiterbar sein, weil wir ständig wachsen.
Der bisherigen Flyer ist im Querformat gehalten- da wir eine hohe Weiterempfehlungsrate haben, hatten wir den so gestaltet, dass er fast wie eine EInladung aussieht, also mit dem Ziel, dass man uns weiterempfiehlt un dabei den Flyer übergibt. Das nur als Info, müssen dabei nicht bleiben. Den alten Flyer haben wir zur Information mit hochgeladen.
- allgemein:
a) Info zu Geschichte, Architektur und Unterhaltung (wenn mögl. auch auf Englisch: Info about History, Architecture and Entertainment
b) Details: Wann: ganzjährig Dauer: 3 Stunden Leistung: 7 Kostproben und Broschüre
Preis: 33€, Kinden 16,50€
auf english: When: all year round Length: 3 hours Includse 7 food samples + guide Price 33€, for children 16,50€
- Überschrift: Kulinarisch-kulturelle Touren
- evtl. noch Teaser: 7 Kostproben in 3 Stunden
Wir denken, es ist zurzeit zu viel Text. Es können Bausteine weg gelassen werden. Sind gespannt auf Eure Ideen.
Es kann auch ein anderes Format als bisher genommen werden.
Wenn möglich bitte unsere Schriften verwenden (siehe Dateiupload)

```html
<!DOCTYPE html>
<html lang="de">
<head>
<meta charset="utf-8">
<title>taste-the-town – Kulinarisch-kulturelle Touren</title>
<link rel="stylesheet" href="https://fonts.googleapis.com/css2?family=Merienda:wght@700&family=Alegreya+Sans+SC:wght@500&family=Alegreya+Sans:wght@500&display=swap">
<style>
  :root{
    --wine:#7e1416;
    --orange:#f6a01a;
    --amber:#f4a522;
    --cream:#fdf1e0;
    --sky:#8cc3ea;
    --sky-light:#e4f2fc;
    --grass:#6fae3a;
    --paper:#ececec;
    --white:#ffffff;
  }
  *{margin:0;padding:0;box-sizing:border-box}
  html,body{width:1200px;height:1200px;overflow:hidden;background:var(--paper)}
  .sheet{position:relative;width:1200px;height:1200px}
  .flyer{position:absolute;left:50px;width:1097px;height:511px;overflow:hidden}
  .flyer--front{top:68px;background:linear-gradient(90deg,var(--white),var(--cream))}
  .flyer--back{top:619px;background:var(--amber)}
  .shape{position:absolute;inset:0;width:100%;height:100%}
  .hand{font-family:"Merienda",cursive;font-weight:700;font-style:normal}
  .caps{font-family:"Alegreya Sans SC",sans-serif;font-weight:500}
  .plain{font-family:"Alegreya Sans",sans-serif;font-weight:500}
  .abs{position:absolute}

  /* front */
  .brand{left:677px;top:26px;width:260px;text-align:center}
  .brand-dot{display:block;width:100px;height:100px;margin:0 auto;border-radius:50%;background:var(--wine)}
  .brand-name{display:block;margin-top:8px;font-size:24px;line-height:26px;color:var(--wine)}
  .kicker{right:35px;top:200px;font-size:39px;line-height:1;color:var(--orange);letter-spacing:-1px}
  .title{right:32px;top:201px;font-size:168px;line-height:1;color:var(--wine);letter-spacing:-7px}
  .teaser{right:35px;top:356px;font-size:23px;line-height:1;color:var(--orange)}
  .cities{left:548px;width:520px;top:392px;text-align:center;font-size:15.8px;line-height:20.5px;color:var(--wine)}
  .tagline{right:35px;top:470px;font-size:10.5px;color:var(--wine);text-transform:uppercase;letter-spacing:-.2px}

  /* back */
  .heading{font-size:32px;color:var(--wine);letter-spacing:-1px;text-align:right}
  .topics{font-size:16px;line-height:17px;color:var(--white);text-align:right}
  .rule{position:absolute;border-top:2px dotted var(--wine);height:0}
  .fact{width:120px}
  .fact dt{font-size:16px;color:var(--wine);line-height:17px}
  .fact dd{font-size:13px;color:var(--white);line-height:15px;letter-spacing:-.3px}
  .fact--right{text-align:right}
  .fact--left{text-align:left;width:160px}
  .divider{position:absolute;border-left:2px dotted var(--white);width:0}
  .gift-a{right:30px;top:308px;font-size:22px;line-height:1.2;color:var(--white);letter-spacing:-1px}
  .gift-b{right:30px;top:332px;font-size:31px;line-height:1.2;color:var(--white);letter-spacing:-1px}
  .tickets{right:36px;top:392px;font-size:36px;color:var(--wine);letter-spacing:-1px}
  .contact{right:36px;top:440px;font-size:18px;color:var(--white);letter-spacing:-.3px}
  .guide-call{left:170px;top:166px;width:130px;text-align:center;font-size:11.5px;line-height:12.5px;transform:rotate(-5deg)}
  .guide-call .q{display:block;color:var(--white)}
  .guide-call .a{display:block;color:var(--wine);margin-top:4px}
</style>
</head>
<body>
<main class="sheet">

  <section class="flyer flyer--front" aria-label="Vorderseite">
    <svg class="shape" viewBox="0 0 1097 511" preserveAspectRatio="none">
      <defs>
        <radialGradient id="scene" cx="0.4" cy="0.35" r="0.75">
          <stop offset="0" stop-color="#d8c38a"/>
          <stop offset="0.45" stop-color="#c9b06a"/>
          <stop offset="0.7" stop-color="var(--grass)"/>
          <stop offset="1" stop-color="var(--sky)"/>
        </radialGradient>
      </defs>
      <path d="M0 0H428Q608 255 475 511H0Z" fill="var(--wine)"/>
      <path d="M0 0H378Q606 255 468 511H0Z" fill="var(--orange)"/>
      <path d="M0 0H370Q600 255 466 511H0Z" fill="var(--sky-light)"/>
      <path d="M0 0H340Q590 255 462 511H0Z" fill="url(#scene)" role="img" aria-label="Rucksack mit Isomatte und Landkarte auf einer Grasinsel, davor belegte Brothäppchen"/>
    </svg>

    <div class="abs brand">
      <span class="brand-dot"></span>
      <span class="brand-name plain">taste-the-town</span>
    </div>

    <h1 class="abs title hand">Touren</h1>
    <p class="abs kicker hand">Kulinarisch-kulturelle</p>
    <p class="abs teaser hand">7 Kostproben in 3 Stunden</p>
    <p class="abs cities caps">In Augsburg, Bamberg, Berlin, Bonn, Bremen, Dresden, Düsseldorf,<br>Essen, Frankfurt, Hamburg, Hannover, Köln, Leipzig, München, Münster,<br>Nürnberg, Oldenburg, Potsdam, Regensburg und Stuttgart</p>
    <p class="abs tagline plain">Walking food tour with 7 samples in 3 hours</p>
  </section>

  <section class="flyer flyer--back" aria-label="Rückseite">
    <svg class="shape" viewBox="0 0 1097 511" preserveAspectRatio="none">
      <defs>
        <linearGradient id="friends" x1="0" y1="0" x2="1" y2="1">
          <stop offset="0" stop-color="#e9d4c4"/><stop offset="0.6" stop-color="#c9a07a"/><stop offset="1" stop-color="#8fa9c8"/>
        </linearGradient>
        <linearGradient id="snacks" x1="0" y1="0" x2="1" y2="1">
          <stop offset="0" stop-color="#f4e3b8"/><stop offset="0.5" stop-color="#e6c27a"/><stop offset="1" stop-color="#4e7a35"/>
        </linearGradient>
        <linearGradient id="couple" x1="0" y1="0" x2="0" y2="1">
          <stop offset="0" stop-color="#8a6b5a"/><stop offset="0.5" stop-color="#d8c8bc"/><stop offset="1" stop-color="#f2efe9"/>
        </linearGradient>
      </defs>
      <path d="M0 0H497Q658 255 495 511H0Z" fill="var(--white)"/>
      <path d="M0 0H467Q654 255 493 511H0Z" fill="var(--wine)"/>
      <path d="M0 0H447Q631 255 478 511H0Z" fill="url(#couple)" role="img" aria-label="Älteres Paar lacht beim Probieren von Häppchen in einer Altstadtgasse"/>
      <rect x="0" y="0" width="296" height="261" fill="url(#friends)" role="img" aria-label="Drei junge Frauen mit Stadtführer bei einer Tour"/>
      <rect x="0" y="264" width="326" height="247" fill="url(#snacks)" role="img" aria-label="Gefüllte Pfannkuchenröllchen mit Schinken und Spinat auf Spießen"/>
      <path d="M298 0V262H0" fill="none" stroke="var(--wine)" stroke-width="4"/>
      <path d="M328 262V511" stroke="var(--wine)" stroke-width="4"/>
      <path d="M296 150V260H162Q170 172 296 150Z" fill="var(--orange)"/>
      <g transform="rotate(-7 718 362)">
        <rect x="585" y="315" width="268" height="96" rx="6" fill="var(--white)"/>
        <rect x="585" y="315" width="140" height="96" rx="6" fill="#5c8d3c" role="img" aria-label="Gutscheinkarte mit Foto von Tomaten und Basilikum"/>
        <rect x="700" y="362" width="153" height="30" fill="var(--wine)"/>
        <text x="782" y="383" fill="var(--white)" font-family="Merienda, cursive" font-weight="700" font-size="13">Gutschein</text>
      </g>
    </svg>

    <p class="abs guide-call hand"><span class="q">Möchten<br>Sie auch Gäste<br>begeistern?</span><span class="a">Bewerben Sie sich<br>als Tourguide!</span></p>

    <div class="abs" style="right:290px;top:40px">
      <h2 class="heading hand">Info zu</h2>
      <p class="topics caps">Geschichte<br>Architektur &amp; Unterhaltung</p>
    </div>
    <div class="abs" style="right:30px;top:40px">
      <h2 class="heading hand">Info about</h2>
      <p class="topics caps">History<br>Architecture &amp; Entertainment</p>
    </div>

    <h2 class="abs heading hand" style="right:30px;top:127px">Details</h2>
    <div class="rule" style="left:571px;width:375px;top:153px"></div>

    <dl class="abs fact fact--right plain" style="left:530px;top:174px"><dt class="caps">Wann</dt><dd>Ganzjährig</dd></dl>
    <dl class="abs fact fact--left plain" style="left:669px;top:174px"><dt class="caps">Leistung</dt><dd>7 Kostproben und Broschüre</dd></dl>
    <dl class="abs fact fact--right plain" style="left:530px;top:224px"><dt class="caps">Dauer</dt><dd>3 Stunden</dd></dl>
    <dl class="abs fact fact--left plain" style="left:669px;top:224px"><dt class="caps">Preis</dt><dd>33€, Kinder 16,50€</dd></dl>
    <div class="divider" style="left:658px;top:178px;height:85px"></div>

    <dl class="abs fact fact--right plain" style="left:792px;top:174px"><dt class="caps">When</dt><dd>All year round</dd></dl>
    <dl class="abs fact fact--left plain" style="left:931px;top:174px"><dt class="caps">Include</dt><dd>7 food samples + guide</dd></dl>
    <dl class="abs fact fact--right plain" style="left:792px;top:224px"><dt class="caps">Lenght</dt><dd>3 hours</dd></dl>
    <dl class="abs fact fact--left plain" style="left:931px;top:224px"><dt class="caps">Preis</dt><dd>33€, for Children 16,50€</dd></dl>
    <div class="divider" style="left:920px;top:178px;height:85px"></div>

    <div class="rule" style="left:578px;width:490px;top:276px"></div>

    <p class="abs gift-a hand">Verschenken Sie uns</p>
    <p class="abs gift-b hand">als Gutschein</p>
    <p class="abs tickets hand">Tickets Online</p>
    <p class="abs contact plain">www.taste-the-town.com • Tel +49 (0) 30 - 555 01 234 0</p>
  </section>

</main>
</body>
</html>
```